Corporate Two Sided Business Card

Looking for a Corporate "edgy" Modern look and feel for a business card

We are looking at two options. Dark background with our logo on it, white background with our logo on it - The background is more - Charcoal / Graphite then black

Details will be

Danielle Forsk

Licensee / Director

m. 0428 519 064

e. danielle@quorvela.com.au

quorvela.com.au

Target Market(s)

Professional Business people that refer use business and clients that own Investment Properties

Industry/Entity Type

Business

Contact Information for Business Card

Details will be

Danielle Forsk

Licensee / Director

m. 0428 519 064

quorvela.com.au

Font styles to use
Serif

Colors
000000
ec1f27
eeeeee
ffffff

Requirements
Must have
• Two options - White Background and Dark Background. - Two sided
Nice to have
• A design that is edgy, modern and new to look instead of boring style corporate cards - It should be a full integrated design
Should not have
• Block looking - Cheap.

```html
<!DOCTYPE html>
<html lang="en">
<head>
<meta charset="utf-8">
<title>Quorvela – Business Card</title>
<link href="https://fonts.googleapis.com/css2?family=Montserrat:wght@400;700&display=swap" rel="stylesheet">
<style>
  :root {
    --stage: #0f0f0f;
    --card: #1c1c1c;
    --card-edge: #232323;
    --brand-red: #ec1f27;
    --text-white: #ffffff;
    --text-soft: #eeeeee;
  }
  * { margin: 0; padding: 0; box-sizing: border-box; }
  html, body {
    width: 1200px;
    height: 1000px;
    overflow: hidden;
    background: var(--stage);
    font-family: "Montserrat", sans-serif;
  }
  .canvas {
    position: relative;
    width: 1200px;
    height: 1000px;
  }
  .card {
    position: absolute;
    width: 480px;
    height: 292px;
    border-radius: 22px;
    background: linear-gradient(135deg, var(--card-edge) 0%, var(--card) 55%, #191919 100%);
    box-shadow: 0 12px 30px rgba(0, 0, 0, 0.55);
  }
  .card--back { left: 90px; top: 250px; }
  .card--front { left: 630px; top: 440px; }

  .wordmark {
    display: flex;
    align-items: center;
    gap: 10px;
    color: var(--text-white);
    font-weight: 700;
    letter-spacing: 0.5px;
    line-height: 1;
  }
  .wordmark__mark {
    width: 18px;
    height: 18px;
    background: var(--brand-red);
  }
  .card--back .wordmark {
    position: absolute;
    left: 50%;
    top: 50%;
    transform: translate(-50%, -50%);
    font-size: 40px;
  }
  .card--front .wordmark {
    position: absolute;
    left: 40px;
    top: 38px;
    font-size: 40px;
  }

  .contact-block {
    position: absolute;
    left: 40px;
    top: 116px;
  }
  .person-name {
    color: var(--brand-red);
    font-weight: 700;
    font-size: 24px;
    line-height: 1.1;
  }
  .person-role {
    color: var(--text-soft);
    font-size: 13px;
    margin-top: 4px;
  }
  .contact-list {
    list-style: none;
    margin-top: 22px;
    color: var(--text-soft);
    font-size: 14px;
    line-height: 1.35;
  }
</style>
</head>
<body>
<main class="canvas">
  <section class="card card--back" aria-label="Card back">
    <div class="wordmark"><span class="wordmark__mark"></span>quorvela</div>
  </section>

  <section class="card card--front" aria-label="Card front">
    <div class="wordmark"><span class="wordmark__mark"></span>quorvela</div>
    <div class="contact-block">
      <p class="person-name">Danielle Forsk</p>
      <p class="person-role">Licensee / Director</p>
      <ul class="contact-list">
        <li>0428 519 064</li>
        <li>danielle@quorvela.com.au</li>
        <li>quorvela.com.au</li>
      </ul>
    </div>
  </section>
</main>
</body>
</html>
```